K7 Digital Stationery Design Project

We are looking to have stationary designs created for our company branding materials. We are looking for the following to be created.
1. Business Cards (front & back)
2. Letterhead
3. Envelopes #10
We are a new web design, development and marketing firm. Primary color scheme is desired to be blue/grey/white. This web start-up is owned and operated by individuals with 15+ years experience each in the industry so should not look as though it is a start-up by young/inexperienced individuals.
We build website & custom applications/software. In addition we provide the full spectrum of web marketing solutions including SEO, PPC, Social Media, Branding, Content Marketing and PR.
Please let us know if you have any questions. Looking forward to seeing all the amazing design ideas.
Attached is our logo.
Thanks!
Target Market(s)
Company will be nearly 100% business to business sales. Looking to work with companies that are already established, with a website, who want to take their website and/or online marketing efforts to the next level.
Industry/Entity Type
Marketing
Look and feel

```html
<!DOCTYPE html>
<html lang="en">
<head>
<meta charset="utf-8">
<title>K7 Digital Stationery</title>
<link href="https://fonts.googleapis.com/css2?family=PT+Sans:wght@400;700&family=Great+Vibes&display=swap" rel="stylesheet">
<style>
  :root {
    --bg: #d8d8d8;
    --paper: #f4f4f4;
    --blue: #1a9fd0;
    --navy: #1d5fa8;
    --charcoal: #2f3033;
    --bar: #3a3b3e;
    --ink: #3c3c3c;
    --muted: #7a7a7a;
    --faint: #dde3ea;
  }
  * { box-sizing: border-box; margin: 0; padding: 0; }
  html, body { width: 1200px; height: 840px; overflow: hidden; }
  body { background: var(--bg); font-family: "PT Sans", Arial, sans-serif; color: var(--ink); position: relative; }

  .sheet { position: absolute; background: var(--paper); box-shadow: 0 6px 18px rgba(0,0,0,.18); overflow: hidden; }
  .stripe { position: absolute; left: 0; top: 0; bottom: 0; width: 8px; background: var(--blue); }

  .brand { display: flex; align-items: center; gap: 7px; font-weight: 700; color: var(--navy); letter-spacing: .5px; }
  .brand-dot { width: 14px; height: 14px; border-radius: 50%; background: var(--navy); }
  .tagline { font-size: 7px; color: var(--muted); margin-top: 2px; }

  .web-bar { display: flex; align-items: center; height: 12px; border-radius: 6px; background: var(--bar); color: #e8e8e8; font-size: 7px; padding-left: 14px; position: relative; }
  .web-bar::before { content: ""; position: absolute; left: 3px; top: 3px; width: 6px; height: 6px; border-radius: 50%; background: var(--blue); }

  /* Letterhead */
  .letterhead { left: 50px; top: 116px; width: 430px; height: 608px; }
  .letterhead .brand { position: absolute; left: 40px; top: 40px; font-size: 17px; }
  .letterhead .tagline { position: absolute; left: 40px; top: 64px; }
  .letterhead .contact { position: absolute; right: 28px; top: 40px; width: 140px; font-size: 7px; line-height: 11px; color: var(--ink); }
  .letterhead .contact .web-bar { margin-top: 4px; }
  .watermark { position: absolute; right: 40px; bottom: 40px; width: 170px; height: 170px; border-radius: 50%; background: var(--faint); }
  .letter { position: absolute; left: 40px; top: 110px; width: 350px; font-size: 9px; line-height: 13px; color: #555; }
  .letter .greeting { font-weight: 700; color: var(--ink); margin-bottom: 10px; }
  .letter p { margin-bottom: 10px; }
  .signature { position: absolute; left: 40px; top: 470px; }
  .signature .sign { font-family: "Great Vibes", cursive; font-size: 26px; color: var(--ink); }
  .signature .role { font-size: 8px; font-weight: 700; color: var(--ink); }

  /* Business cards */
  .card { top: 116px; width: 300px; height: 171px; background: var(--charcoal); }
  .card .stripe { width: 7px; }
  .card-front { left: 530px; }
  .card-front .brand { position: absolute; left: 0; right: 0; top: 58px; justify-content: center; font-size: 18px; color: var(--blue); }
  .card-front .tagline { position: absolute; left: 0; right: 0; top: 84px; text-align: center; color: #a8a8a8; }
  .card-front .web { position: absolute; right: 16px; bottom: 16px; font-size: 8px; color: #cfcfcf; }
  .card-back { left: 870px; }
  .card-back .mark { position: absolute; left: 28px; top: 30px; width: 46px; height: 46px; border-radius: 50%; background: var(--navy); }
  .card-back .person { position: absolute; left: 110px; top: 28px; }
  .card-back .name { font-size: 13px; color: var(--blue); font-weight: 700; }
  .card-back .title { font-size: 8px; color: #c8c8c8; }
  .card-back .details { position: absolute; left: 110px; top: 70px; list-style: none; font-size: 8px; color: #d8d8d8; }
  .card-back .details li { display: flex; align-items: center; gap: 6px; height: 17px; }
  .card-back .details svg { width: 9px; height: 9px; flex: none; }

  /* Envelope */
  .envelope { left: 530px; top: 330px; width: 620px; height: 269px; }
  .envelope .stripe { width: 9px; }
  .envelope .sender { position: absolute; left: 36px; top: 32px; width: 170px; }
  .envelope .brand { font-size: 17px; }
  .envelope .address { font-size: 7px; color: var(--ink); margin: 8px 0 4px; }
</style>
</head>
<body>

  <section class="sheet letterhead" aria-label="Letterhead">
    <div class="stripe"></div>
    <div class="brand"><span class="brand-dot"></span>K7 DIGITAL</div>
    <div class="tagline">Web Design, Development and Marketing</div>
    <div class="contact">
      <div>t (555) 014 2280</div>
      <div>f (555) 014 2291</div>
      <div>e hello@k7digital.com</div>
      <div>12 Harbor Lane, Westport, Ohio</div>
      <div class="web-bar">www.k7digital.com</div>
    </div>
    <div class="watermark"></div>
    <div class="letter">
      <div class="greeting">Lorem ipsum,</div>
      <p>Cras mattis consectetur purus sit amet fermentum. Etiam porta sem malesuada magna mollis euismod. Integer posuere erat a ante venenatis dapibus posuere velit aliquet.</p>
      <p>Vivamus sagittis lacus vel augue laoreet rutrum faucibus dolor auctor. Donec sed odio dui. Nullam id dolor id nibh ultricies vehicula ut id elit.</p>
      <p>Donec id elit non mi porta gravida at eget metus. Fusce dapibus, tellus ac cursus commodo, tortor mauris condimentum nibh, ut fermentum massa justo sit amet risus.</p>
      <p>Cum sociis natoque penatibus et magnis dis parturient montes, nascetur ridiculus mus. Curabitur blandit tempus porttitor.</p>
      <p>Cras justo odio, dapibus ac facilisis in, egestas eget quam. Morbi leo risus, porta ac consectetur ac, vestibulum at eros.</p>
    </div>
    <div class="signature">
      <div class="sign">Your Name</div>
      <div class="role">Company Director</div>
    </div>
  </section>

  <section class="sheet card card-front" aria-label="Business card front">
    <div class="stripe"></div>
    <div class="brand"><span class="brand-dot"></span>K7 DIGITAL</div>
    <div class="tagline">Web Design, Development and Marketing</div>
    <div class="web">www.k7digital.com</div>
  </section>

  <section class="sheet card card-back" aria-label="Business card back">
    <div class="stripe"></div>
    <div class="mark"></div>
    <div class="person">
      <div class="name">Lena Marsh</div>
      <div class="title">Operation Manager</div>
    </div>
    <ul class="details">
      <li><svg viewBox="0 0 10 10"><circle cx="5" cy="5" r="4" fill="none" stroke="#1a9fd0" stroke-width="1.4"/></svg>t (555) 014 2280</li>
      <li><svg viewBox="0 0 10 10"><circle cx="5" cy="5" r="4" fill="none" stroke="#1a9fd0" stroke-width="1.4"/></svg>f (555) 014 2291</li>
      <li><svg viewBox="0 0 10 10"><circle cx="5" cy="5" r="4" fill="none" stroke="#1a9fd0" stroke-width="1.4"/></svg>e hello@k7digital.com</li>
      <li><svg viewBox="0 0 10 10"><circle cx="5" cy="5" r="4" fill="none" stroke="#1a9fd0" stroke-width="1.4"/></svg>12 Harbor Lane, Westport, Ohio</li>
    </ul>
  </section>

  <section class="sheet envelope" aria-label="Envelope #10">
    <div class="stripe"></div>
    <div class="sender">
      <div class="brand"><span class="brand-dot"></span>K7 DIGITAL</div>
      <div class="address">12 Harbor Lane, Westport, Ohio</div>
      <div class="web-bar">www.k7digital.com</div>
    </div>
  </section>

</body>
</html>
```